Hello,
We’re looking for a new WordPress website for Gather Your Light, our company offering unique well-being retreats and workshops.
We currently have a website online (you can consult it : www.gatheryourlight.ch), but we now need to build a new site on WordPress — more flexible, more intuitive to manage, and better aligned with our evolving needs.

What we’re looking for:
A new userfriendly WordPress site, with:
Inspiring, elegant, and modern design
Smooth user experience on desktop and mobile
Innovative design proposals – we want to be inspired !
SEO best practices
Respect of our existing color palette
The final website will need to be set up on our existing hosting provider (details can be shared later)

Pages to Include:
- Home
- Our Story
- Our Stays - with links to 5 individual pages, each describing one of our stays in detail.
- Activities – with potential links to individual descriptive pages
- Agenda
- Our Charter
- The Team
- Contact
- Blog

Required Features:
- Space for photos and videos
- Sections for testimonials and press articles
- Blog/article layout with strong readability
- Easy-to-update backend for future content
- Newsletter sign-up (pop-up and in footer)
- Additional pop-up on/off
- “Request info” buttons
- “Booking request” buttons
- Integration of our 4 pillars - Breathe · Feel · Connect · Experience - in the design (They’re currently in the footer, but we’re open to creative suggestions)

Who we are :
Gather Your Light offers well-being and personal growth stays but with a very different spirit.
We’re not a classic wellness brand. Our approach is professional, joyful, and grounded.
We create spaces where people can take a real break — breathe, slow down, and reconnect with themselves.
During our stays, people are welcomed like friends:
with warmth, respect, and no pressure.
Each program combines practices like breathwork, movement, creativity, coaching, and massages in a relaxed, beautiful setting of the French Alps.
What makes us different:
A friendly and down-to-earth atmosphere
A wide mix of activities.
A mix of inner work and simple pleasures
Private rooms, nourishing food, and shared moments
Time to talk, to laugh, to walk, or just be silent together - and feel free to be yourself
Our guests come to pause.
They leave feeling lighter, aligned, and full of life

```html
<!DOCTYPE html>
<html lang="en">
<head>
<meta charset="utf-8">
<title>Gather Your Light — Home</title>
<link href="https://fonts.googleapis.com/css2?family=Montserrat:wght@400;500;600;700&family=Lora:wght@400;500&display=swap" rel="stylesheet">
<style>
:root{
  --backdrop:#9aaaa9;
  --navy:#23407a;
  --teal:#5dbdb8;
  --teal-soft:#e6f5f4;
  --ink:#1f1f1f;
  --muted:#6d6d6d;
  --line:#d9e7e6;
  --paper:#ffffff;
  --mist:#f6f4f4;
  --night:#050505;
}
*{box-sizing:border-box;margin:0;padding:0}
html,body{width:1200px;height:4286px;overflow:hidden}
body{background:var(--backdrop);font-family:"Montserrat",sans-serif;color:var(--ink)}
.page{position:absolute;left:78px;top:67px;width:1045px;height:4153px;background:var(--paper);overflow:hidden}
.abs{position:absolute}
.serif{font-family:"Lora",serif}
.kicker{color:var(--teal);font-size:11px;font-weight:600;letter-spacing:.5px;text-transform:uppercase}
.btn{display:inline-flex;align-items:center;justify-content:center;border-radius:20px;font-size:9px;font-weight:600;text-transform:uppercase;letter-spacing:.4px}
.btn-outline{border:1.5px solid var(--teal);color:var(--ink);background:#fff}
.btn-dark{background:#000;color:#fff;text-transform:none;font-size:10px}
.ph{position:absolute}

/* header */
.site-header{position:absolute;left:0;top:0;width:1045px;height:90px;z-index:3}
.brand{position:absolute;left:26px;top:26px;font-weight:700;font-size:26px;color:var(--navy);letter-spacing:.5px}
.nav{position:absolute;left:476px;top:13px;display:flex;gap:21px;font-size:10px;color:#222}
.nav span{padding:3px 0}
.nav .current{border-bottom:1.5px solid var(--teal)}
.nav .nav-contact{border:1.5px solid var(--navy);padding:3px 8px}

/* hero */
.hero{position:absolute;left:0;top:0;width:1045px;height:600px;background:linear-gradient(180deg,#eef2f3 0%,#f6ecd8 32%,#f3cf93 48%,#c6c4c0 58%,#8d9299 70%,#b49a7f 82%,#d6c3a8 100%)}
.hero-title{position:absolute;left:0;width:942px;top:278px;text-align:center;font-size:30px;line-height:37px;font-weight:400;color:#1a1a1a}
.hero-btn{position:absolute;left:408px;top:367px;width:122px;height:22px;border:1.5px solid var(--teal);background:rgba(255,255,255,.75);font-size:8.5px}
.hero-curve{position:absolute;left:0;top:500px}
.pillar{position:absolute;width:166px;height:166px;border-radius:50%;background:#fff;top:507px}
.pillar .art{position:absolute;left:38px;top:22px;width:90px;height:70px;border-radius:40%}
.pillar .label{position:absolute;left:0;width:166px;top:105px;text-align:center;font-family:"Lora",serif;font-size:14px;letter-spacing:.5px;color:#8a7e8e;text-transform:uppercase}

/* story */
.story-kicker{left:168px;top:716px}
.story-title{left:168px;top:738px;font-size:28px;line-height:34px;font-weight:400;width:380px}
.story-lead{left:168px;top:828px;font-size:9px;font-weight:500}
.story-text{left:168px;top:851px;font-size:9px;line-height:14px;color:#444;width:280px}
.story-actions{left:168px;top:918px;display:flex;align-items:center;gap:18px;font-size:9px}
.story-actions .btn{width:100px;height:26px}
.phone{display:flex;align-items:center;gap:8px}

.purpose-kicker{left:0;width:1045px;text-align:center;top:1044px}
.purpose-title{left:0;width:1045px;top:1066px;text-align:center;font-size:28px;line-height:34px;font-weight:400}
.purpose-name{left:0;width:1045px;top:1188px;text-align:center;font-size:11px}
.purpose-role{left:0;width:1045px;top:1205px;text-align:center;font-size:8.5px;color:var(--muted)}

/* activities */
.activity{position:absolute;width:136px;height:118px;border:1.5px solid var(--line);border-radius:22px;text-align:center;padding-top:14px}
.activity h3{color:var(--teal);font-size:13px;font-weight:600}
.activity p{font-size:9px;line-height:11px;color:#444;margin-top:3px}
.activity .badge{position:absolute;left:48px;width:40px;height:40px;border-radius:50%;border:1.5px solid var(--line);background:#fff}
.activity.low{padding-top:36px}

/* agenda */
.agenda-kicker{left:554px;top:1900px}
.agenda-title{left:554px;top:1924px;font-size:28px;line-height:34px;font-weight:400;width:340px}
.agenda-text{left:554px;top:1999px;font-size:9px;line-height:14px;width:270px;color:#333}
.month-open{left:554px;top:2053px;width:260px;height:61px;border:1.5px solid var(--teal);border-radius:10px;padding:8px 12px}
.month-open b{display:block;color:var(--teal);font-size:11px}
.month-open span{font-size:8.5px;line-height:12px;display:block;margin-top:2px}
.month{left:554px;width:260px;height:25px;border-radius:13px;background:var(--teal);color:#fff;font-size:11px;font-weight:700;padding:0 12px;display:flex;align-items:center;justify-content:space-between}
.month i{width:12px;height:12px;border-radius:50%;background:#fff;position:relative;display:block}
.month i::after{content:"";position:absolute;left:3px;top:5px;width:6px;height:2px;background:var(--teal)}
.month i::before{content:"";position:absolute;left:5px;top:3px;width:2px;height:6px;background:var(--teal)}
.agenda-actions{left:554px;top:2246px;display:flex;gap:14px}
.agenda-actions .btn{height:26px}

/* testimonial */
.avatar{left:482px;top:2810px;width:84px;height:84px;border-radius:50%;background:linear-gradient(160deg,#e2ddd7,#b9b1a8)}
.arrow-btn{width:36px;height:36px;border-radius:50%;border:1.5px solid #ccc;background:#fff;top:2970px}
.quote-text{left:300px;width:445px;top:2962px;text-align:center;font-size:9.5px;line-height:13px;color:#333}
.quote-name{left:0;width:1045px;top:3066px;text-align:center;font-size:10px}
.quote-role{left:0;width:1045px;top:3081px;text-align:center;font-size:8px;color:var(--muted)}
.dots{left:500px;top:3100px;display:flex;gap:7px}
.dots span{width:5px;height:5px;border-radius:50%;background:#c9d7d6}
.dots .on{background:var(--teal)}

/* news */
.news{left:0;top:3075px;width:1045px;height:453px;background:var(--mist)}
.news-kicker{left:0;width:1045px;top:121px;text-align:center;font-family:"Lora",serif;font-size:7px;letter-spacing:1px}
.news-title{left:0;width:1045px;top:136px;text-align:center;font-family:"Lora",serif;font-size:25px;font-weight:400}
.card{position:absolute;top:207px;width:225px;height:266px;background:#fff}
.card .pic{position:absolute;left:0;top:0;width:225px;height:166px}
.card .date{position:absolute;right:10px;top:142px;width:36px;height:42px;background:#000;color:#fff;text-align:center;font-family:"Lora",serif;font-size:15px;line-height:20px;padding-top:4px}
.card .date small{display:block;font-size:5px;line-height:6px}
.card .meta{position:absolute;left:20px;top:192px;font-family:"Lora",serif;font-size:6px;letter-spacing:.5px}
.card .meta em{color:#aaa;font-style:normal}
.card h4{position:absolute;left:20px;top:207px;width:175px;font-family:"Lora",serif;font-weight:400;font-size:12px;line-height:16px}
.news-dot{left:519px;top:3645px;width:4px;height:4px;border-radius:50%;background:#333}

/* contact */
.contact-kicker{left:168px;top:3590px;font-family:"Lora",serif;font-size:7px;letter-spacing:1px}
.contact-title{left:168px;top:3608px;font-family:"Lora",serif;font-size:25px;line-height:31px;font-weight:400}
.contact-text{left:168px;top:3683px;width:260px;font-size:8.5px;line-height:14px;color:#777}
.contact-line{left:168px;display:flex;gap:12px;font-size:8px;color:#777;align-items:center}
.field{position:absolute;height:22px;border-bottom:1px solid #e1e1e1;font-size:8px;color:#999;display:flex;align-items:center;gap:8px}
.send{left:528px;top:3790px;width:113px;height:26px;border-radius:13px;background:var(--teal);color:#fff;font-family:"Lora",serif;font-size:6.5px;letter-spacing:1px}
.consent{left:667px;top:3797px;font-size:7px;color:#999;display:flex;gap:6px;align-items:center}
.consent i{width:8px;height:8px;border:1px solid #999;display:block}
.consent u{color:var(--teal)}

/* social strip */
.strip{left:0;top:3886px;width:1045px;height:191px;display:flex}
.strip div{flex:1}
.strip-badge{left:494px;top:3956px;width:52px;height:52px;border-radius:50%;background:#fff}

/* footer */
.footer{left:0;top:4077px;width:1045px;height:76px;background:var(--night)}
.footer .copy{position:absolute;left:168px;top:34px;font-size:7px;color:#fff}
.footer .foot-brand{position:absolute;left:0;width:1045px;top:24px;text-align:center;font-weight:700;font-size:22px;color:var(--teal)}
.footer .social{position:absolute;left:768px;top:29px;display:flex;gap:9px}
.footer .social span{width:19px;height:19px;border-radius:4px;background:#fff;display:block}
</style>
</head>
<body>
<main class="page">

  <!-- Hero -->
  <section class="hero" role="img" aria-label="Traveller with a hat and backpack raising his arms on a rocky lake shore at sunset, with mountains across the water and drifting dandelion seeds"></section>

  <header class="site-header">
    <div class="brand">Gather Your Light</div>
    <nav class="nav">
      <span class="current">Home</span><span>Our Story</span><span>Our Stays</span><span>Activities</span><span>Agenda</span><span>Our Charter</span><span>The Team</span><span>Blog</span><span class="nav-contact">Contact</span>
    </nav>
  </header>

  <h1 class="hero-title">Take a break<br>Gather your light</h1>
  <a class="btn hero-btn">Booking request</a>

  <svg class="hero-curve" width="1045" height="100" viewBox="0 0 1045 100">
    <path d="M0 40 C150 70 300 95 520 98 C760 100 900 70 1045 20 L1045 100 L0 100 Z" fill="#fff"/>
  </svg>

  <div class="pillar" style="left:163px">
    <div class="art" role="img" aria-label="Pillar illustration: a soft cloud blown by a breath" style="background:radial-gradient(circle,#e8dcd4 55%,#fff 72%)"></div>
    <div class="label">Breathe</div>
  </div>
  <div class="pillar" style="left:346px">
    <div class="art" role="img" aria-label="Pillar illustration: a red burst of fireworks" style="background:radial-gradient(circle,#f3b3b3 30%,#fff 70%)"></div>
    <div class="label">Feel</div>
  </div>
  <div class="pillar" style="left:529px">
    <div class="art" role="img" aria-label="Pillar illustration: a heart made of two puzzle pieces" style="background:radial-gradient(circle,#ea5a77 35%,#fff 70%)"></div>
    <div class="label">Connect</div>
  </div>
  <div class="pillar" style="left:716px">
    <div class="art" role="img" aria-label="Pillar illustration: bare feet standing in green grass" style="background:radial-gradient(circle,#8fc79a 35%,#fff 70%)"></div>
    <div class="label">Experience</div>
  </div>

  <!-- Our story -->
  <p class="abs kicker story-kicker">Our Story</p>
  <h2 class="abs story-title">We welcome everyone<br>in our community.</h2>
  <p class="abs story-lead">We have a strong sense of community.</p>
  <p class="abs story-text">Adults and children of all ages here are encouraged to learn about their own faith and the role of God in their everyday life and in the general sense.</p>
  <div class="abs story-actions">
    <a class="btn btn-outline">Learn more</a>
    <span class="phone">
      <svg width="16" height="16" viewBox="0 0 16 16"><circle cx="8" cy="8" r="7.5" fill="none" stroke="#ccc"/><path d="M5.5 4.5l1.5 0 .7 2-1 .8a5 5 0 0 0 2 2l.8-1 2 .7v1.5c-3 .5-6.5-3-6-6z" fill="none" stroke="#333" stroke-width=".8"/></svg>
      +41 21 555 01 20
    </span>
  </div>
  <div class="ph" role="img" aria-label="Woman with closed eyes framed by large green leaves" style="left:694px;top:684px;width:182px;height:195px;background:linear-gradient(150deg,#3f6f6a,#86a89d 55%,#d2b49c);border-radius:6px"></div>
  <div class="ph" role="img" aria-label="Young woman breathing calmly outdoors with her face to the sun" style="left:591px;top:802px;width:183px;height:180px;background:linear-gradient(160deg,#c7d3a9,#e7d2b6 60%,#b8906f);border-radius:6px"></div>

  <p class="abs kicker purpose-kicker">Our Purpose</p>
  <h2 class="abs purpose-title">We are helping people to find<br>love and courage in their hearts to live with<br>dignity and purpose.</h2>
  <p class="abs purpose-name">Elian Marsh</p>
  <p class="abs purpose-role">Community Leader</p>

  <!-- Photo strip -->
  <div class="ph" role="img" aria-label="Woman sitting cross-legged on a mat in a bright room" style="left:0;top:1248px;width:262px;height:356px;background:linear-gradient(180deg,#e4e2dd,#b47a84 65%,#6b3a45)"></div>
  <div class="ph" role="img" aria-label="Guests sharing a meal on a terrace with a lake and mountain view" style="left:262px;top:1248px;width:261px;height:356px;background:linear-gradient(180deg,#a8bfd2,#e8e4dc 55%,#a9a296)"></div>
  <div class="ph" role="img" aria-label="Candlelit meditation circle with cushions and a gong" style="left:523px;top:1248px;width:261px;height:356px;background:linear-gradient(180deg,#c9c1a3,#7a6a3c 55%,#e2c66b)"></div>
  <div class="ph" role="img" aria-label="Chef plating colourful dishes in a kitchen" style="left:784px;top:1248px;width:261px;height:356px;background:linear-gradient(180deg,#d8d9d6,#a9a8a2 55%,#4f4f4c)"></div>

  <!-- Activities -->
  <svg class="abs" style="left:168px;top:1692px" width="710" height="140" viewBox="0 0 710 140">
    <path d="M140 70 h24 M282 70 h24 M424 70 h24 M566 70 h24" stroke="#d9e7e6" stroke-width="1.5"/>
  </svg>
  <div class="activity" style="left:168px;top:1700px"><h3>Breathwork</h3><p>Lorem ipsum dolor<br>sit amet,<br>consectetuer<br>adipiscing elit.</p><span class="badge" style="top:96px"></span></div>
  <div class="activity low" style="left:310px;top:1700px"><span class="badge" style="top:-18px"></span><h3>Workshops</h3><p>Lorem ipsum<br>dolor sit amet,<br>consectetuer<br>adipiscing elit.</p></div>
  <div class="activity" style="left:452px;top:1700px"><h3>Movement</h3><p>Lorem ipsum<br>dolor sit amet,<br>consectetuer<br>adipiscing elit.</p><span class="badge" style="top:96px"></span></div>
  <div class="activity low" style="left:594px;top:1700px"><span class="badge" style="top:-18px"></span><h3>Massage</h3><p>Lorem ipsum<br>dolor sit amet,<br>consectetuer<br>adipiscing elit.</p></div>
  <div class="activity" style="left:736px;top:1700px"><h3>Coaching</h3><p>Lorem ipsum<br>dolor sit amet,<br>consectetuer<br>adipiscing elit.</p><span class="badge" style="top:96px"></span></div>

  <!-- Agenda -->
  <div class="ph" role="img" aria-label="Dried flowers in a metal milk can under a chandelier" style="left:168px;top:1889px;width:168px;height:195px;background:linear-gradient(170deg,#8d8a83,#c9c7c1 60%,#6a6157);border-radius:6px"></div>
  <div class="ph" role="img" aria-label="Plated starter decorated with edible flowers on a lawn" style="left:349px;top:1889px;width:168px;height:195px;background:linear-gradient(170deg,#7ea35a,#c5d1a6 55%,#f0e9d8);border-radius:6px"></div>
  <div class="ph" role="img" aria-label="Private bedroom with a made bed and red lamp" style="left:168px;top:2098px;width:168px;height:195px;background:linear-gradient(170deg,#e9e8e6,#cfcac6 60%,#9b8f8a);border-radius:6px"></div>
  <div class="ph" role="img" aria-label="Wooden sauna interior" style="left:349px;top:2098px;width:168px;height:195px;background:linear-gradient(170deg,#e4dccf,#c3ad8e 60%,#8d7558);border-radius:6px"></div>

  <p class="abs kicker agenda-kicker" style="text-transform:none">L'Agenda</p>
  <h2 class="abs agenda-title">We build the world of<br>peace together.</h2>
  <p class="abs agenda-text">Our community focuses on finding inner balance between body and mind and creating harmony around by building it inside.</p>
  <div class="abs month-open"><b>AVRIL 2025</b><span><strong>ECHAPPÉE:</strong> du vendredi 18 avril au lundi 21 avril – COMPLET</span></div>
  <div class="abs month" style="top:2125px">MAI 2025<i></i></div>
  <div class="abs month" style="top:2160px">JUIN 2025<i></i></div>
  <div class="abs month" style="top:2195px">JUILLET 2025<i></i></div>
  <div class="abs agenda-actions">
    <a class="btn btn-outline" style="width:94px">Learn more</a>
    <a class="btn btn-dark" style="width:128px">Request Information</a>
  </div>

  <!-- Video -->
  <div class="ph" role="img" aria-label="Video still: woman playing a singing bowl on a pebble beach" style="left:0;top:2366px;width:1045px;height:384px;background:linear-gradient(120deg,#9aa1a6,#d8d3cc 35%,#e9dccf 55%,#a4a5a2 80%,#c5c2bc)"></div>
  <svg class="abs" style="left:476px;top:2512px" width="92" height="92" viewBox="0 0 92 92">
    <circle cx="46" cy="46" r="44" fill="none" stroke="#fff" stroke-width="2"/>
    <path d="M38 31 L62 46 L38 61 Z" fill="#fff"/>
  </svg>

  <!-- Testimonial -->
  <div class="ph avatar" role="img" aria-label="Portrait photo of the retreat participant"></div>
  <svg class="abs arrow-btn" style="left:168px" viewBox="0 0 36 36"><path d="M23 18H13M17 14l-4 4 4 4" fill="none" stroke="#333" stroke-width="1.3"/></svg>
  <svg class="abs arrow-btn" style="left:839px" viewBox="0 0 36 36"><path d="M13 18h10M19 14l4 4-4 4" fill="none" stroke="#333" stroke-width="1.3"/></svg>
  <p class="abs quote-text">This is one of the most exciting parts where we get to express our appreciation as members of this amazing community. Thank you for all your hard work regarding our health and great mood!</p>
  <svg class="abs" style="left:508px;top:3030px" width="28" height="22" viewBox="0 0 28 22"><path d="M3 4c4 0 7 3 7 7s-3 7-7 7c2-3 2-5 0-7M17 4c4 0 7 3 7 7s-3 7-7 7c2-3 2-5 0-7" fill="none" stroke="#5dbdb8" stroke-width="3"/></svg>
  <p class="abs quote-name">Nora Vial</p>
  <p class="abs quote-role">Retreat Participant</p>
  <div class="abs dots"><span></span><span class="on"></span><span></span><span></span></div>

  <!-- News -->
  <section class="abs news">
    <p class="abs news-kicker">LEARN MORE</p>
    <h2 class="abs news-title">Our Latest News</h2>
    <article class="card" style="left:168px">
      <div class="pic" role="img" aria-label="Three women holding hand-written peace signs in a forest" style="background:linear-gradient(170deg,#8aa26c,#ece7df 55%,#6d7a64)"></div>
      <div class="date">13<small>APR</small></div>
      <p class="meta">RELIGION · <em>0 Comments</em></p>
      <h4>Get out and vote for “peace and love” this election day</h4>
    </article>
    <article class="card" style="left:410px">
      <div class="pic" role="img" aria-label="Massage session on a sandy beach" style="background:linear-gradient(170deg,#d9b8a2,#efe6dc 50%,#c45c47)"></div>
      <div class="date">13<small>APR</small></div>
      <p class="meta">RELIGION · <em>0 Comments</em></p>
      <h4>Outdated yoga “rules” we need more now than ever</h4>
    </article>
    <article class="card" style="left:650px">
      <div class="pic" role="img" aria-label="White church next to a modern glass tower under a blue sky" style="background:linear-gradient(170deg,#4f8ed0,#a9c9ea 45%,#e8e5df)"></div>
      <div class="date">12<small>APR</small></div>
      <p class="meta">RELIGION · <em>0 Comments</em></p>
      <h4>Reasons to make time for yoga when you’re too busy</h4>
    </article>
  </section>
  <span class="abs news-dot"></span>

  <!-- Contact -->
  <p class="abs contact-kicker">CONTACT US</p>
  <h2 class="abs contact-title">Have Questions?<br>Get in touch!</h2>
  <p class="abs contact-text">In case you gave any questions about our community, you are welcome to write us.</p>
  <div class="abs contact-line" style="top:3733px">
    <svg width="10" height="12" viewBox="0 0 10 12"><path d="M5 11C2 7 1 5.5 1 4a4 4 0 0 1 8 0c0 1.5-1 3-4 7z" fill="none" stroke="#5dbdb8"/><circle cx="5" cy="4" r="1.3" fill="#5dbdb8"/></svg>12 Rue des Tilleuls, Annecy</div>
  <div class="abs contact-line" style="top:3761px;color:#333">
    <svg width="10" height="12" viewBox="0 0 10 12"><rect x="2" y="1" width="6" height="10" rx="1" fill="none" stroke="#5dbdb8"/></svg>+33 4 50 00 12 34</div>
  <div class="abs contact-line" style="top:3788px">
    <svg width="10" height="12" viewBox="0 0 10 12"><rect x="0.5" y="2.5" width="9" height="7" fill="none" stroke="#5dbdb8"/><path d="M.5 2.5l4.5 4 4.5-4" fill="none" stroke="#5dbdb8"/></svg>hello@gatheryourlight.ch</div>

  <div class="field" style="left:528px;top:3612px;width:168px">
    <svg width="9" height="10" viewBox="0 0 9 10"><circle cx="4.5" cy="3" r="2.3" fill="none" stroke="#999"/><path d="M.5 10c0-3 8-3 8 0" fill="none" stroke="#999"/></svg>Name</div>
  <div class="field" style="left:709px;top:3612px;width:168px">
    <svg width="10" height="8" viewBox="0 0 10 8"><rect x=".5" y=".5" width="9" height="7" fill="none" stroke="#999"/><path d="M.5.5l4.5 4 4.5-4" fill="none" stroke="#999"/></svg>Email Address</div>
  <div class="field" style="left:528px;top:3660px;width:168px">
    <svg width="10" height="10" viewBox="0 0 10 10"><path d="M2 1l2 .2.5 2-1 .8a4 4 0 0 0 2 2l.8-1 2 .5V7.5C5 8 1.5 5 2 1z" fill="none" stroke="#999"/></svg>Phone</div>
  <div class="field" style="left:709px;top:3660px;width:168px">
    <svg width="10" height="10" viewBox="0 0 10 10"><circle cx="5" cy="5" r="4.3" fill="none" stroke="#999"/><path d="M5 4v3.5" stroke="#999"/></svg>Subject</div>
  <div class="field" style="left:528px;top:3708px;width:349px;height:44px;align-items:flex-start;padding-top:6px">
    <svg width="10" height="10" viewBox="0 0 10 10"><path d="M1 9l1-3 5-5 2 2-5 5z" fill="none" stroke="#999"/></svg>How can we help you? Feel free to get in touch!</div>
  <a class="abs btn send">GET IN TOUCH</a>
  <div class="abs consent"><i></i>I agree that my data is <u>collected and stored</u>.</div>

  <!-- Social strip -->
  <div class="abs strip">
    <div role="img" aria-label="Dandelion seed head close-up with a hand-lettered thank-you" style="background:linear-gradient(160deg,#6f8a57,#c7c2a8 60%,#7a6b4a)"></div>
    <div role="img" aria-label="Forest bathing promotional post with sunlight through trees" style="background:linear-gradient(160deg,#3e4a2a,#a77a3a 55%,#2f2a1e)"></div>
    <div role="img" aria-label="Soft-focus blossoms with a hand-lettered well-being message" style="background:linear-gradient(160deg,#c49a73,#e4cdb3 55%,#a8825f)"></div>
    <div role="img" aria-label="Teal poster with a dandelion and a hand-lettered invitation" style="background:linear-gradient(160deg,#5d8d94,#9cb8b4 55%,#537f86)"></div>
    <div role="img" aria-label="Spring energy post with a person resting on grass" style="background:linear-gradient(160deg,#7c8a7c,#a9b3a2 55%,#5b6b4f)"></div>
    <div role="img" aria-label="Breathing exercises card on a warm textured background" style="background:linear-gradient(160deg,#8b6d5a,#d9c8b8 55%,#9d7b63)"></div>
  </div>
  <div class="abs strip-badge"></div>

  <!-- Footer -->
  <footer class="abs footer">
    <p class="copy">Gather Your Light © 2025. All Rights Reserved.</p>
    <div class="foot-brand">Gather Your Light</div>
    <div class="social"><span></span><span></span><span></span><span></span></div>
  </footer>

</main>
</body>
</html>
```